International Honeymoon Tour Operator needs Business Card

We need to design a business card including our new logo for a new tour operator called Marisol Thorne Getaways. We would like to also include the text 'Personal Tailor-Made Honeymoons for our Guests at a Lower Cost'. Please Include the following details as well; 'Website: www.marisolthornegetaways.co.uk'; 'E-mail: felix@marisolthornegetaways.co.uk'; 'Mobile: 07914263058'. We would like the design to be compatible with the logo and text. The final design should communicate professionalism, modern and ethical.

We want to business card to be double sided.

We would like to be able to easily adjust the e-mail address and contact number in the future for other employees either through you or ourselves.

Target Market(s)

Brides and grooms aged 18-35 predominantly.

Industry/Entity Type

Business

Colors

Designer to choose colors to be used in the design.

Requirements
Must have
• Logo
Requested Text
Double sided
Nice to have
• Additional colour
The wow factor
Should not have
• Images of currency

```html
<!DOCTYPE html>
<html lang="en">
<head>
<meta charset="utf-8">
<title>Marisol Thorne Getaways – Business Card</title>
<link href="https://fonts.googleapis.com/css2?family=Raleway:wght@300;400&family=Arimo&family=Tinos:ital@1&display=swap" rel="stylesheet">
<style>
  :root{
    --stage:#4b7269;
    --card:#d6e3d2;
    --band:#648a80;
    --rim:#e6eae5;
    --heart:#ffffff;
    --deep:#2f5f55;
    --leaf:#8cc63f;
    --white:#ffffff;
  }
  *{margin:0;padding:0;box-sizing:border-box}
  html,body{width:1200px;height:1000px;overflow:hidden;background:var(--stage)}
  .canvas{position:relative;width:1200px;height:1000px}
  .card{position:absolute;left:325px;width:525px;background:var(--card);overflow:hidden;
        box-shadow:0 2px 6px rgba(0,0,0,.18)}
  .card--front{top:135px;height:341px}
  .card--back{top:526px;height:340px}
  .heart{position:absolute;display:block}
  .card--front .heart{left:115px;top:20px;width:292px;height:250px}
  .card--back .heart{left:78px;top:14px;width:370px;height:318px}
  .tagline-band{position:absolute;left:0;right:0;top:248px;height:93px;background:var(--band);
        display:flex;align-items:center;justify-content:center;text-align:center}
  .tagline{font-family:'Tinos',serif;font-style:italic;color:var(--white);font-size:21px;line-height:24px;margin-top:-2px}
  .brand{position:absolute;left:115px;width:292px;top:118px;text-align:center;
        font-family:'Raleway',sans-serif;font-weight:300;color:var(--deep);font-size:30px;line-height:34px}
  .contact{position:absolute;left:0;right:0;top:60px;text-align:center}
  .contact-label{font-family:'Raleway',sans-serif;font-weight:300;color:var(--leaf);font-size:36px;line-height:38px}
  .contact-value{font-family:'Arimo',sans-serif;color:var(--deep);font-size:16px;line-height:18px;margin-bottom:17px}
</style>
</head>
<body>
<div class="canvas">

  <section class="card card--front">
    <svg class="heart" viewBox="0 0 100 90" preserveAspectRatio="none" aria-hidden="true">
      <path d="M50 89 C20 66 0 46 0 26 C0 10 12 0 26 0 C38 0 46 7 50 15 C54 7 62 0 74 0 C88 0 100 10 100 26 C100 46 80 66 50 89 Z"
            fill="var(--rim)" stroke="#ffffff" stroke-width=".5" stroke-dasharray="1.2 .8"/>
      <path transform="translate(4 4) scale(.92)" d="M50 89 C20 66 0 46 0 26 C0 10 12 0 26 0 C38 0 46 7 50 15 C54 7 62 0 74 0 C88 0 100 10 100 26 C100 46 80 66 50 89 Z" fill="var(--heart)"/>
    </svg>
    <div class="brand">Marisol Thorne<br>Getaways</div>
    <div class="tagline-band">
      <p class="tagline">Personal Tailor-Made Honeymoons for<br>our Guests at a Lower Cost</p>
    </div>
  </section>

  <section class="card card--back">
    <svg class="heart" viewBox="0 0 100 90" preserveAspectRatio="none" aria-hidden="true">
      <path d="M50 89 C20 66 0 46 0 26 C0 10 12 0 26 0 C38 0 46 7 50 15 C54 7 62 0 74 0 C88 0 100 10 100 26 C100 46 80 66 50 89 Z"
            fill="var(--rim)" stroke="#ffffff" stroke-width=".4" stroke-dasharray="1 .7"/>
      <path transform="translate(3.5 3.5) scale(.93)" d="M50 89 C20 66 0 46 0 26 C0 10 12 0 26 0 C38 0 46 7 50 15 C54 7 62 0 74 0 C88 0 100 10 100 26 C100 46 80 66 50 89 Z" fill="var(--heart)"/>
    </svg>
    <div class="contact">
      <p class="contact-label">Website</p>
      <p class="contact-value">www.marisolthornegetaways.co.uk</p>
      <p class="contact-label">Email</p>
      <p class="contact-value">felix@marisolthornegetaways.co.uk</p>
      <p class="contact-label">Mobile</p>
      <p class="contact-value">+44 (0)7914263058</p>
    </div>
  </section>

</div>
</body>
</html>
```